The Gilded Otter Espresso Nook Coffee Card

would like a coffee card designed for our café. Most cards are so boring and I need to stand out from the crowd (The Gilded Otter ). I require our logo on one side or the business name also a place for people to write their name and mobile number (collecting data base) and on the back the following
customer gets a stamp for the 1st three coffees purchased, on the 3rd one they get a free upsize. another 2 stamps and on the 3rd one (6) gets a free coffee, another 2 stamps and the customer gets another upsize (9th coffee purchased) and on the 10th card they recivie a voucher for a free pizza.
small print | one free pizza for dinner dining (not available for takeaways and must book), Cant be used with any other offers, opts in to hear from the herd if there is a deal on. cant trade for cash or gift

```html
<!DOCTYPE html>
<html lang="en">
<head>
<meta charset="utf-8">
<title>The Gilded Otter Espresso Nook – Coffee Card</title>
<link rel="stylesheet" href="https://fonts.googleapis.com/css2?family=Open+Sans:wght@400;600&family=Teko:wght@400;500;600&display=swap">
<style>
  :root {
    --page: #e9e4de;
    --card-white: #ffffff;
    --ink: #1b1b1b;
    --text: #333333;
    --brown: #6b4a37;
    --brown-soft: #7a5742;
    --rule: #d4d4d4;
  }
  * { box-sizing: border-box; margin: 0; padding: 0; }
  html, body { width: 900px; height: 1200px; overflow: hidden; }
  body { background: var(--page); position: relative; font-family: "Open Sans", sans-serif; color: var(--text); }

  .card { position: absolute; left: 87px; width: 734px; height: 428px; border-radius: 22px; overflow: hidden; box-shadow: 0 6px 14px rgba(0,0,0,.25); }
  .card-front { top: 137px; background: var(--card-white); }
  .card-back { top: 634px; background: var(--brown); }

  .brand-name { position: absolute; left: 52px; top: 44px; font-family: "Teko", sans-serif; font-weight: 500; font-size: 66px; line-height: 1; letter-spacing: -0.5px; color: var(--ink); white-space: nowrap; }
  .brand-rule { position: absolute; left: 53px; top: 112px; width: 295px; height: 1px; background: var(--rule); }
  .brand-tagline { position: absolute; left: 53px; top: 122px; width: 295px; text-align: center; font-size: 15px; letter-spacing: .5px; color: var(--text); }

  .address { position: absolute; left: 52px; top: 154px; font-size: 14.5px; line-height: 22px; }
  .contact-list { position: absolute; left: 52px; top: 212px; list-style: none; font-size: 14.5px; line-height: 19px; }
  .contact-list li { display: flex; align-items: center; gap: 17px; }
  .contact-list svg { width: 12px; height: 12px; fill: var(--brown); flex: none; }

  .field { position: absolute; left: 52px; font-size: 17px; font-weight: 600; color: var(--text); letter-spacing: .4px; white-space: nowrap; }
  .field-name { top: 305px; }
  .field-mobile { top: 350px; }

  .mark-area { position: absolute; left: 443px; top: 206px; width: 238px; height: 170px; background: var(--ink); border-radius: 40px 60px 30px 30px; }

  .front-band { position: absolute; left: 0; bottom: 0; width: 100%; height: 27px; background: var(--brown); }
  .front-band-gap { position: absolute; left: 365px; bottom: 0; width: 4px; height: 27px; background: var(--card-white); }

  .faint-mark { position: absolute; left: 105px; top: 30px; width: 530px; height: 370px; background: var(--brown-soft); border-radius: 90px 120px 40px 40px; }

  .stamps { position: absolute; left: 25px; top: 190px; display: flex; gap: 20px; list-style: none; }
  .stamp { width: 50px; height: 50px; border-radius: 50%; background: var(--card-white); display: flex; align-items: center; justify-content: center; }
  .stamp-count { border: 3px solid var(--ink); font-family: "Teko", sans-serif; font-weight: 600; font-size: 44px; line-height: 1; color: var(--ink); padding-top: 6px; }
  .stamp-reward span { transform: rotate(-55deg); font-family: "Teko", sans-serif; font-weight: 600; font-size: 13px; line-height: 11px; color: var(--brown); text-align: center; letter-spacing: .3px; }
</style>
</head>
<body>

<section class="card card-front" aria-label="Coffee card front">
  <h1 class="brand-name">THE GILDED OTTER</h1>
  <div class="brand-rule"></div>
  <p class="brand-tagline">ESPRESSO NOOK</p>

  <address class="address" style="font-style:normal">48 Willow Bend Rd., at The Boathouse<br>Millbrook, VT 05901</address>

  <ul class="contact-list">
    <li><svg viewBox="0 0 12 12"><path d="M2.5 0.5l2 2.5-1.2 1.2c.7 1.6 1.9 2.8 3.5 3.5L8 6.5l2.5 2-1 2.2C5 10.5 1.3 6.8 1 2.5z"/></svg>1-555-204-7781</li>
    <li><svg viewBox="0 0 12 12"><path d="M0 2h12v1.2L6 7 0 3.2z M0 4.6l6 3.8 6-3.8V10H0z"/></svg>gildedottercafe@mailbox.com</li>
    <li><svg viewBox="0 0 12 12"><circle cx="6" cy="6" r="5.2" fill="none" stroke="#6b4a37" stroke-width="1"/><path d="M0.8 6h10.4M6 0.8v10.4" stroke="#6b4a37" stroke-width="1"/><ellipse cx="6" cy="6" rx="2.4" ry="5.2" fill="none" stroke="#6b4a37" stroke-width="1"/></svg>www.gildedottercafe.com</li>
  </ul>

  <p class="field field-name">Name: ___________________________</p>
  <p class="field field-mobile">Mobile: _________________________</p>

  <div class="mark-area" role="img" aria-label="Café mascot silhouette"></div>

  <div class="front-band"></div>
  <div class="front-band-gap"></div>
</section>

<section class="card card-back" aria-label="Coffee card back: stamp rewards">
  <div class="faint-mark" role="img" aria-label="Faint café mascot silhouette"></div>
  <ol class="stamps">
    <li class="stamp stamp-count">1</li>
    <li class="stamp stamp-count">2</li>
    <li class="stamp stamp-reward"><span>UPSIZE</span></li>
    <li class="stamp stamp-count">4</li>
    <li class="stamp stamp-count">5</li>
    <li class="stamp stamp-reward"><span>FREE<br>COFFEE</span></li>
    <li class="stamp stamp-count">7</li>
    <li class="stamp stamp-count">8</li>
    <li class="stamp stamp-reward"><span>UPSIZE</span></li>
    <li class="stamp stamp-reward"><span>FREE<br>PIZZA</span></li>
  </ol>
</section>

</body>
</html>
```